4x8 Billing Insert Advertising VOIP Services

We need a double-sided 4x8 inch billing insert advertisement describing our Hosted PBX services on one side and our Voice Over Internet (VOIP) on the other. Banks, Libraries, Schools, Hospitals and other large businesses on our fiber optic network will look to the Hosted PBX systems (no up front cost to customer) while smaller businesses and residential customers will most likely call about our standard VOIP that can use a normal phone set. Attached is a vendor brochure describing a hosted pbx service that we'd like to take bullet information to create our simpler call to action ad. (We do not currently offer the Mobility package as of yet so no need to include this information in ad.)
We'd like to see designs that use the colors of blue and black and entice current customers to add a phone to their existing fiber internet service while saving money. Final design should create a call to action requesting a quote or call 800-413-2286 for more information about our services. Hosted PBX phone systems are $27/month per premium seat while standard VOIP services are $25/month per phone line (customer can attach any standard phone set such as a residential cordless phone).
Our company website is http://trivalink.example if you need to gather any information from however, we will be redesigning it soon too as well.
Target Market(s)
Our current customers that have our fiber internet service. Schools, Banks, Hospitals, Local and County Government buildings as well as small businesses and residential customers.
Industry/Entity Type
Residential
Requirements
Must have
- An image of the phone set being leased and the service price outlined. A clear call to action message.
Nice to have
- Bullet information about the Hosted PBX or VOIP service. (unlimited long distance in the U.S., voicemail, call waiting, caller id, call forwarding, forward busy, forward no answer, 3-way calling, distinctive ring and many other calling features included.)

```html
<!DOCTYPE html>
<html lang="en">
<head>
<meta charset="utf-8">
<title>Trivalink Billing Insert</title>
<link href="https://fonts.googleapis.com/css2?family=Arimo:wght@400;700&family=Open+Sans:wght@400;700&display=swap" rel="stylesheet">
<style>
  :root {
    --stage: #1b1b1b;
    --paper: #ffffff;
    --brand-blue: #1f6db5;
    --panel-blue: #1f6fb6;
    --ink: #111111;
    --grey-text: #3c3c3c;
    --footer: #060606;
    --badge: #fff200;
    --label: #e6e6e6;
    --photo-dark: #3a3d42;
    --photo-light: #b9bcc1;
  }
  * { box-sizing: border-box; margin: 0; padding: 0; }
  html, body { width: 1200px; height: 1112px; overflow: hidden; background: var(--stage); }
  body { position: relative; font-family: "Arimo", Arial, sans-serif; }

  .side-label {
    position: absolute; top: 66px; width: 451px; text-align: center;
    font-family: "Open Sans", Arial, sans-serif; font-size: 33px; color: var(--label);
  }
  .insert {
    position: absolute; top: 144px; width: 451px; height: 902px;
    background: var(--paper); overflow: hidden;
  }
  .side-one { left: 94px; }
  .side-two { left: 637px; }

  .brand { position: absolute; top: 20px; left: 0; width: 100%; text-align: center; }
  .brand-name {
    display: inline-flex; align-items: center; gap: 12px;
    font-family: "Arimo", Arial, sans-serif; font-weight: 700; font-size: 52px;
    color: var(--brand-blue); letter-spacing: 1px; line-height: 1;
  }
  .brand-dot { width: 46px; height: 46px; border-radius: 50%; background: var(--brand-blue); }
  .brand-tagline { margin-top: 12px; font-size: 20px; font-weight: 700; color: var(--ink); }

  .service-title { position: absolute; line-height: 1.2; }
  .service-title .accent { display: block; color: var(--brand-blue); font-weight: 700; }
  .service-title .plain { display: block; color: var(--grey-text); font-weight: 700; }
  .side-one .service-title { left: 12px; top: 178px; font-size: 32px; }
  .side-two .service-title { right: 22px; top: 212px; text-align: center; font-size: 32px; }
  .side-two .service-title .accent { font-size: 54px; line-height: 1; }

  .photo { position: absolute; border-radius: 10px; }
  .desk-phone {
    left: 222px; top: 168px; width: 202px; height: 188px;
    background: linear-gradient(135deg, var(--photo-dark), #1c1e21 60%, var(--photo-light));
  }
  .cordless-phones {
    left: 14px; top: 186px; width: 226px; height: 194px;
    background: linear-gradient(180deg, #2b2d31, var(--photo-light) 75%, #e3e4e6);
  }

  .price-badge { position: absolute; width: 198px; height: 112px; }
  .side-one .price-badge { left: -4px; top: 276px; }
  .side-two .price-badge { left: 253px; top: 330px; }
  .price-badge svg { position: absolute; inset: 0; }
  .price-text {
    position: absolute; inset: 0; display: flex; flex-direction: column;
    justify-content: center; align-items: center; transform: rotate(-10deg);
    font-family: "Open Sans", Arial, sans-serif; color: var(--ink); line-height: 1.1;
  }
  .price-text .amount { font-size: 25px; font-weight: 700; }
  .price-text .unit { font-size: 19px; }

  .benefits {
    position: absolute; left: 0; top: 418px; width: 100%; height: 362px;
    background: var(--panel-blue); border-top: 6px solid var(--footer); color: var(--paper);
    padding: 14px 24px 0 22px;
  }
  .benefits h2 { font-size: 28px; font-weight: 700; margin-bottom: 22px; }
  .benefits ul { list-style: none; }
  .benefits li {
    position: relative; padding-left: 27px; font-size: 16px; line-height: 21px; margin-bottom: 19px;
  }
  .benefits li::before {
    content: ""; position: absolute; left: 2px; top: 6px; width: 8px; height: 8px; background: var(--paper);
  }

  .call-to-action {
    position: absolute; left: 0; top: 780px; width: 100%; height: 122px;
    background: var(--footer); border-top: 5px solid var(--paper);
    color: var(--paper); text-align: center; font-weight: 700; padding-top: 10px;
  }
  .call-to-action .prompt { font-size: 25px; }
  .call-to-action .number { font-size: 45px; line-height: 1.25; letter-spacing: 0.5px; }
</style>
</head>
<body>
  <div class="side-label" style="left:94px">Side 1</div>
  <div class="side-label" style="left:637px">Side 2</div>

  <section class="insert side-one">
    <header class="brand">
      <div class="brand-name"><span class="brand-dot"></span>TRIVALINK</div>
      <div class="brand-tagline">Internet - Phone - Data</div>
    </header>
    <h1 class="service-title"><span class="accent">Hosted PBX</span><span class="plain">Services</span></h1>
    <div class="photo desk-phone" role="img" aria-label="Photo of a hosted PBX desk phone with colour display and corded handset"></div>
    <div class="price-badge">
      <svg viewBox="0 0 198 112" width="198" height="112" aria-hidden="true">
        <ellipse cx="99" cy="56" rx="97" ry="52" fill="var(--badge)" transform="rotate(-8 99 56)"/>
      </svg>
      <div class="price-text"><span class="amount">$27/month</span><span class="unit">per premium</span></div>
    </div>
    <div class="benefits">
      <h2>Why Choose Us?</h2>
      <ul>
        <li>No upfront cost for equipment and phones</li>
        <li>Bundled price includes everything you need - phone system, long distance, and equipment</li>
        <li>Popular features such as simultaneous ring, auto attendant, hunt groups, and music-on-hold</li>
        <li>Scalable to meet your changing business needs</li>
        <li>Web interface enables yout to change features at a click of a mouse</li>
      </ul>
    </div>
    <footer class="call-to-action">
      <div class="prompt">Call Us to Request a Quote</div>
      <div class="number">800-413-2286</div>
    </footer>
  </section>

  <section class="insert side-two">
    <header class="brand">
      <div class="brand-name"><span class="brand-dot"></span>TRIVALINK</div>
      <div class="brand-tagline">Internet - Phone - Data</div>
    </header>
    <div class="photo cordless-phones" role="img" aria-label="Photo of two cordless home phones in their charging bases"></div>
    <h1 class="service-title"><span class="accent">VOIP</span><span class="plain">Services</span></h1>
    <div class="price-badge">
      <svg viewBox="0 0 198 112" width="198" height="112" aria-hidden="true">
        <ellipse cx="99" cy="56" rx="97" ry="50" fill="var(--badge)" transform="rotate(-10 99 56)"/>
      </svg>
      <div class="price-text"><span class="amount">$25/month</span><span class="unit">per premium</span></div>
    </div>
    <div class="benefits">
      <h2>Why Choose Us?</h2>
      <ul>
        <li>Unlimited long distance in the U.S</li>
        <li>Bundled price includes everything you need - phone system, long distance, and equipment</li>
        <li>Popular features such as voicemail,&nbsp; call waiting, caller id, call forwarding&nbsp; and many other calling features included.</li>
        <li>Distinctive Ring</li>
        <li>3-way Calling</li>
      </ul>
    </div>
    <footer class="call-to-action">
      <div class="prompt">Call Us to Request a Quote</div>
      <div class="number">800-413-2286</div>
    </footer>
  </section>
</body>
</html>
```